KFO R Training Website

We need a website to post videos, blogs and other information or links.
We teach Jujitsu , combatives, Metaphysical Coaching. I want to tach online and in person. Silver Heron Institute Deals in several areas of Personal Protection and Coaching.
Training (Martial Arts / combative)
Emotional Intelligence
Leadership Development
Motivation
Our Log is attached.
Similar Websites to what we do ( we want to stand out better).
https://marcovelden.example/
https://raybusko.example/
https://summitfusionmentoring.example/
Industry/Entity Type
Training , Martial Arts, coaching
Coding
Coded - Design and coding required
Number of Pages Required
2 page
Look and feel

```html
<!DOCTYPE html>
<html lang="en">
<head>
<meta charset="utf-8">
<title>Silver Heron Institute</title>
<link rel="stylesheet" href="https://fonts.googleapis.com/css2?family=Montserrat:wght@600;700;800&family=Questrial&display=swap">
<style>
:root{
  --red:#ee1c25;
  --red-bright:#ff2a33;
  --ink:#111111;
  --text:#2a2a2a;
  --white:#ffffff;
  --grey-bg:#eeecec;
  --footer:#111111;
  --card-shadow:rgba(0,0,0,.12);
}
*{margin:0;padding:0;box-sizing:border-box}
html,body{width:1200px;height:4095px;overflow:hidden}
body{position:relative;background:var(--white);font-family:"Questrial",sans-serif;color:var(--text)}
.abs{position:absolute}
.heading{font-family:"Montserrat",sans-serif;font-weight:800;color:var(--ink);text-align:center;letter-spacing:.5px}
.divider{position:absolute;left:50%;width:76px;height:2px;margin-left:-38px;background:var(--red)}
.divider::after{content:"";position:absolute;left:50%;top:-3px;width:8px;height:8px;margin-left:-4px;border-radius:50%;background:var(--red)}
.lead{position:absolute;text-align:center;font-size:15px;line-height:24px;color:var(--text)}
.btn{position:absolute;display:flex;align-items:center;justify-content:center;font-family:"Montserrat",sans-serif;font-weight:700;font-size:13px;font-variant:small-caps;letter-spacing:.5px;border-radius:3px;text-decoration:none}
.btn-red{background:var(--red);color:var(--white)}
.btn-white{background:var(--white);color:var(--red)}

/* hero */
.hero{position:absolute;left:0;top:0;width:1200px;height:639px;overflow:hidden}
.hero-photo{position:absolute;inset:0;background:linear-gradient(180deg,#6d4a63 0%,#d47a3f 22%,#f2a83a 30%,#c2693c 40%,#4d4258 58%,#1c2030 78%,#0d0f17 100%)}
.hero-brand{position:absolute;left:111px;top:44px;width:110px;text-align:center;color:var(--white);font-family:"Questrial",sans-serif;font-size:12px;line-height:14px}
.hero-brand .mark{display:block;width:18px;height:18px;margin:0 auto 4px;border:2px solid var(--white);border-radius:50%}
.nav{position:absolute;left:444px;top:46px;display:flex;gap:28px;font-size:15px;color:var(--white)}
.nav a{color:var(--white);text-decoration:none}
.hero-title{position:absolute;right:112px;top:210px;font-family:"Montserrat",sans-serif;font-weight:800;font-size:52px;color:var(--white);letter-spacing:1px}
.hero-text{position:absolute;right:112px;top:286px;width:440px;text-align:right;font-size:17px;line-height:24px;color:var(--white)}
.dots{position:absolute;left:1133px;top:274px}
.dots span{position:absolute;left:0;width:13px;height:13px;border:2px solid var(--white);border-radius:50%}

/* mission */
.video{position:absolute;overflow:hidden;border:3px solid #1a1a1a}
.video.active{border-color:var(--red);z-index:2}
.play{position:absolute;left:50%;top:50%;width:30px;height:30px;margin:-15px 0 0 -15px;border-radius:50%;background:var(--red)}
.play::after{content:"";position:absolute;left:12px;top:9px;border-left:10px solid var(--white);border-top:6px solid transparent;border-bottom:6px solid transparent}

/* about */
.about{position:absolute;left:0;top:1490px;width:1200px;height:585px;background:linear-gradient(135deg,#ff2f37 0%,#ee1c25 55%,#d9161f 100%)}
.about-brand{position:absolute;left:108px;top:150px;width:424px;text-align:center;color:var(--white)}
.about-brand .mark{display:block;width:150px;height:150px;margin:0 auto 40px;border:10px solid var(--white);border-radius:50%}
.about-brand .name{font-family:"Montserrat",sans-serif;font-weight:700;font-size:34px;line-height:40px}
.about-title{position:absolute;left:599px;top:120px;font-family:"Montserrat",sans-serif;font-weight:800;font-size:34px;color:var(--white)}
.about-rule{position:absolute;left:599px;top:170px;width:96px;height:2px;background:var(--white)}
.about-text{position:absolute;left:599px;width:468px;font-size:17px;line-height:24px;color:var(--white);text-align:justify}

/* services */
.service{position:absolute;top:2312px;width:230px;height:219px;background:var(--white);box-shadow:0 2px 10px var(--card-shadow);text-align:center}
.service .icon{position:absolute;left:72px;top:22px;width:86px;height:86px;border-radius:50%;background:var(--red)}
.service .label{position:absolute;left:0;right:0;top:130px;font-size:22px;line-height:24px;font-variant:small-caps;color:#222;letter-spacing:.5px}

/* focus */
.focus{position:absolute;left:0;top:2619px;width:1200px;height:980px;background:var(--grey-bg)}
.cell{position:absolute;width:327px;height:252px}
.cell.text{background:var(--white);text-align:center;padding:38px 24px 0}
.cell h3{font-family:"Montserrat",sans-serif;font-weight:700;font-size:19px;color:var(--ink);letter-spacing:.5px;margin-bottom:14px}
.cell p{font-size:15px;line-height:24px;color:var(--text)}
.cell .more{display:inline-block;margin-top:14px;font-family:"Montserrat",sans-serif;font-weight:700;font-size:18px;font-variant:small-caps;color:var(--red)}

/* signup */
.signup-title{position:absolute;left:453px;top:3546px;font-family:"Montserrat",sans-serif;font-weight:800;font-size:28px;line-height:34px;color:var(--white);letter-spacing:.5px}
.signup-text{position:absolute;left:450px;top:3620px;width:500px;font-size:12px;line-height:17px;color:var(--white)}
.signup-form{position:absolute;left:450px;top:3658px;width:496px;height:36px;border:2px solid var(--white);border-radius:18px;background:var(--white)}
.signup-form .field{position:absolute;left:14px;top:9px;font-family:"Montserrat",sans-serif;font-weight:700;font-size:12px;font-variant:small-caps;color:#222}
.signup-form .submit{position:absolute;right:0;top:0;width:100px;height:32px;border-radius:16px;background:var(--red);color:var(--white);font-family:"Montserrat",sans-serif;font-weight:700;font-size:12px;font-variant:small-caps;display:flex;align-items:center;justify-content:center}

/* footer */
.footer{position:absolute;left:0;top:3599px;width:1200px;height:496px;background:var(--footer)}
.foot-brand{position:absolute;left:110px;top:3787px;width:214px;text-align:center;color:var(--white)}
.foot-brand .mark{display:block;width:78px;height:78px;margin:0 auto 18px;border:6px solid var(--white);border-radius:50%}
.foot-brand .name{font-family:"Montserrat",sans-serif;font-weight:700;font-size:19px;line-height:24px}
.foot-col{position:absolute;top:3787px;color:var(--white)}
.foot-col h4{font-family:"Montserrat",sans-serif;font-weight:800;font-size:18px;margin-bottom:8px}
.foot-col li{list-style:none;font-size:15px;line-height:24px;padding-left:3px}
.contact-row{position:absolute;left:879px;display:flex;gap:14px;font-size:15px;line-height:24px;color:var(--white)}
.social{position:absolute;top:3958px;width:26px;height:26px;border-radius:50%;background:var(--red)}
.copyright{position:absolute;left:0;top:4024px;width:1200px;text-align:center;font-size:14px;color:var(--white)}
</style>
</head>
<body>

<!-- Hero -->
<section class="hero">
  <div class="hero-photo" role="img" aria-label="Silhouettes of climbers helping each other up a mountain ridge at sunset"></div>
  <div class="hero-brand"><span class="mark"></span>Silver Heron Institute</div>
  <nav class="nav">
    <a href="#">Home</a><a href="#">About</a><a href="#">Services</a><a href="#">Products</a><a href="#">Media</a><a href="#">Latest Blog</a>
  </nav>
  <a class="btn btn-red" href="#" style="left:961px;top:35px;width:126px;height:38px;font-size:14px">Contact Us</a>
  <h1 class="hero-title">MOTIVATION</h1>
  <p class="hero-text">Lorem ipsum dolor sit amet, consectetur elit, sed do eiusmod tempor incididunt ut labore et dolore magna aliqua.</p>
  <a class="btn btn-red" href="#" style="left:812px;top:377px;width:143px;height:39px">Teach Online</a>
  <a class="btn btn-white" href="#" style="left:966px;top:377px;width:121px;height:39px">In Person</a>
  <div class="dots">
    <span style="top:0"></span>
    <span style="top:24px"></span>
    <span style="top:48px"></span>
    <span style="top:72px;background:var(--red);border-color:var(--red)"></span>
  </div>
</section>

<!-- Mission -->
<h2 class="heading abs" style="left:0;top:710px;width:1200px;font-size:35px">OUR MISSION</h2>
<div class="divider" style="top:758px"></div>
<p class="lead" style="left:111px;top:778px;width:978px">Lorem ipsum dolor sit amet, consectetur adipiscing elit, sed do eiusmod tempor incididunt ut labore et dolore magna aliqua. Ut enim ad minim veniam, quis nostrud exercitation ullamco laboris nisi ut aliquip ex ea commodo consequat.</p>

<div class="video" style="left:109px;top:888px;width:322px;height:409px;background:linear-gradient(135deg,#8a7a68,#4f4338 60%,#2d2520)" role="img" aria-label="Video still of a woman in a fighting stance"><span class="play"></span></div>
<div class="video" style="left:778px;top:888px;width:311px;height:409px;background:linear-gradient(135deg,#c9c6bf,#8d8477 50%,#3a3330)" role="img" aria-label="Video still of a woman working in a bright office"><span class="play"></span></div>
<div class="video active" style="left:420px;top:863px;width:360px;height:459px;background:linear-gradient(135deg,#e6e1da,#9b8d7e 45%,#3d3630)" role="img" aria-label="Video still of a business team meeting around a table"><span class="play"></span></div>

<a class="btn btn-red" href="#" style="left:527px;top:1365px;width:146px;height:39px">Learn More</a>

<!-- About -->
<section class="about">
  <div class="about-brand">
    <span class="mark"></span>
    <div class="name">Silver Heron Institute</div>
  </div>
  <h2 class="about-title">ABOUT</h2>
  <div class="about-rule"></div>
  <p class="about-text" style="top:190px">Lorem ipsum dolor sit amet, consectetur adipiscing elit, sed do eiusmod tempor incididunt ut labore et dolore magna aliqua. Ut enim ad minim veniam, quis nostrud exercitation ullamco laboris nisi ut aliquip ex ea commodo consequat.</p>
  <p class="about-text" style="top:322px">Lorem ipsum dolor sit amet, consectetur adipiscing elit, sed do eiusmod tempor incididunt ut labore et dolore magna aliqua.</p>
  <a class="btn btn-white" href="#" style="left:599px;top:417px;width:139px;height:38px">Our Services</a>
</section>

<!-- Services -->
<h2 class="heading abs" style="left:0;top:2160px;width:1200px;font-size:35px">OUR SERVICES</h2>
<div class="divider" style="top:2207px"></div>
<p class="lead" style="left:111px;top:2227px;width:978px">Lorem ipsum dolor sit amet, consectetur adipiscing elit, sed do eiusmod tempor incididunt ut labore et dolore magna aliqua. Ut enim ad minim veniam, quis nostrud exercitation ullamco laboris nisi ut aliquip ex ea commodo consequat.</p>

<div class="service" style="left:111px">
  <span class="icon"><svg width="86" height="86" viewBox="0 0 86 86"><circle cx="30" cy="30" r="6" fill="#fff"/><path d="M22 62V42q0-6 8-6t8 6v20z" fill="#fff"/><rect x="42" y="28" width="22" height="16" fill="none" stroke="#fff" stroke-width="3"/><path d="M48 44l-4 14M58 44l4 14" stroke="#fff" stroke-width="3"/></svg></span>
  <div class="label">Training<br>(Martial Arts)</div>
</div>
<div class="service" style="left:360px">
  <span class="icon"><svg width="86" height="86" viewBox="0 0 86 86"><path d="M43 64L24 45a11 11 0 0 1 19-12a11 11 0 0 1 19 12z" fill="#fff"/></svg></span>
  <div class="label">Emotional<br>Intelligence</div>
</div>
<div class="service" style="left:608px">
  <span class="icon"><svg width="86" height="86" viewBox="0 0 86 86" fill="#fff"><circle cx="43" cy="28" r="6"/><circle cx="27" cy="34" r="5"/><circle cx="59" cy="34" r="5"/><path d="M35 62V42q0-5 8-5t8 5v20zM20 60V46q0-4 7-4t7 4v14zM52 60V46q0-4 7-4t7 4v14z"/></svg></span>
  <div class="label">Leadership<br>Development</div>
</div>
<div class="service" style="left:858px">
  <span class="icon"><svg width="86" height="86" viewBox="0 0 86 86" fill="#fff"><rect x="28" y="34" width="30" height="22" rx="6"/><rect x="34" y="56" width="18" height="10"/><path d="M40 22l3 8 3-8zM28 26l6 7 1-3zM58 26l-6 7-1-3z"/></svg></span>
  <div class="label" style="top:142px">Motivation</div>
</div>

<!-- Focus -->
<section class="focus"></section>
<h2 class="heading abs" style="left:0;top:2700px;width:1200px;font-size:35px">OUR FOUCUS AREA</h2>
<div class="divider" style="top:2747px"></div>
<p class="lead" style="left:140px;top:2770px;width:920px;font-size:16px">Lorem ipsum dolor sit amet, consectetur adipiscing elit, sed do eiusmod tempor incididunt ut labore et dolore magna aliqua. Ut enim ad minim veniam, quis nostrud exercitation aliquip ex ea commodo consequat.</p>

<div class="cell" style="left:110px;top:2866px;background:linear-gradient(135deg,#bfc2c6,#5e6c86 55%,#2a3658)" role="img" aria-label="Two students grappling on a jujitsu mat"></div>
<div class="cell text" style="left:437px;top:2866px">
  <h3>COMBATIVE</h3>
  <p>Lorem ipsum dolor sit amet, consectetur adipiscing elit, sed do eiusmod tempor incididunt ut labore et dolore magna aliqua.</p>
  <span class="more">Read More &raquo;</span>
</div>
<div class="cell" style="left:764px;top:2866px;background:radial-gradient(circle at 50% 50%,#fff3c4 0%,#e8a63a 18%,#5a3a7a 50%,#1a1230 100%)" role="img" aria-label="Glowing human figure radiating light in a cosmic field"></div>

<div class="cell text" style="left:110px;top:3118px">
  <h3>JUJITSU</h3>
  <p>Lorem ipsum dolor sit amet, consectetur adipiscing elit, sed do eiusmod tempor incididunt ut labore et dolore magna aliqua.</p>
  <span class="more">Read More &raquo;</span>
</div>
<div class="cell" style="left:437px;top:3118px;background:linear-gradient(180deg,#6f7f91 0%,#b9b3a6 45%,#c9a67a 70%,#a9845a 100%)" role="img" aria-label="Two martial artists sparring on a beach"></div>
<div class="cell text" style="left:764px;top:3118px">
  <h3>METAPHYSICAL</h3>
  <p>Lorem ipsum dolor sit amet, consectetur adipiscing elit, sed do eiusmod tempor incididunt ut labore et dolore magna aliqua.</p>
  <span class="more">Read More &raquo;</span>
</div>

<!-- Footer background -->
<footer class="footer"></footer>

<!-- Signup -->
<svg class="abs" style="left:110px;top:3507px" width="978" height="222" viewBox="0 0 978 222" aria-hidden="true">
  <rect width="978" height="222" fill="#ffffff"/>
  <path d="M330 0H978V222H330Q250 165 268 105Q285 40 330 0z" fill="#ee1c25"/>
</svg>
<div class="abs" style="left:160px;top:3413px;width:220px;height:316px;background:linear-gradient(180deg,#e8e6e3 0%,#3d5f9e 45%,#22407a 100%)" role="img" aria-label="Smiling coach in a blue suit with arms crossed"></div>
<h2 class="signup-title">SIGNING UP FOR FREE STARTER<br>COACHING!</h2>
<p class="signup-text">Lorem ipsum dolor sit amet, consectetur adipiscing elit, sed do eiusmod tempor incididunt ut labore et dolore magna aliqua.</p>
<div class="signup-form"><span class="field">Enter Email</span><span class="submit">Submit</span></div>

<!-- Footer content -->
<div class="foot-brand">
  <span class="mark"></span>
  <div class="name">Silver Heron Institute</div>
</div>
<span class="social" style="left:116px"></span>
<span class="social" style="left:152px"></span>
<span class="social" style="left:189px"></span>
<span class="social" style="left:225px"></span>

<div class="foot-col" style="left:414px">
  <h4>HOME</h4>
  <ul><li>Home</li><li>About</li><li>Services</li><li>Products</li><li>Media</li><li>Latest Blog</li></ul>
</div>
<div class="foot-col" style="left:594px">
  <h4>SERVICES</h4>
  <ul><li style="line-height:32px">Training</li><li style="line-height:32px">Emotional Intelligence</li><li style="line-height:32px">Leadership Development</li><li style="line-height:32px">Motivation</li></ul>
</div>
<div class="foot-col" style="left:879px">
  <h4>CONTACT US</h4>
</div>
<div class="contact-row" style="top:3820px">
  <svg width="20" height="20" viewBox="0 0 20 20"><circle cx="10" cy="10" r="10" fill="#ee1c25"/><path d="M6 5l2 0 1 3-1.5 1a6 6 0 0 0 3.5 3.5l1-1.5 3 1 0 2q-6 1-9-4z" fill="#fff"/></svg>
  <span>+1 888 888 8888</span>
</div>
<div class="contact-row" style="top:3866px">
  <svg width="20" height="20" viewBox="0 0 20 20"><circle cx="10" cy="10" r="10" fill="#ee1c25"/><rect x="5" y="6.5" width="10" height="7" fill="none" stroke="#fff" stroke-width="1.4"/><path d="M5 7l5 4 5-4" fill="none" stroke="#fff" stroke-width="1.4"/></svg>
  <span>info@silverheron.example</span>
</div>
<div class="contact-row" style="top:3905px">
  <svg width="20" height="20" viewBox="0 0 20 20" style="margin-top:12px"><circle cx="10" cy="10" r="10" fill="#ee1c25"/><path d="M10 16q-4-5-4-8a4 4 0 0 1 8 0q0 3-4 8z" fill="#fff"/><circle cx="10" cy="8" r="1.5" fill="#ee1c25"/></svg>
  <span>Lorem ipsum dolor sit amet<br># 640.Lorem</span>
</div>

<p class="copyright">&copy;Copyrights 2022 &nbsp;Silver Heron Institute &nbsp;| &nbsp;All Rights Reserved</p>

</body>
</html>
```